Restaurant menu design

I need a menu for a restaurant in Spain.
It has to be bohemian but modern. We need something romantic and elegant.
The restaurant is elegant with good food and an excellent reputation. It is also modern at the same time.
The restaurant is superbly decorated and very chick so we need something "class" to fit in with the surroundings.
The size of the document must be 325 mm in high and 245 mm as a maximum and preferably made in indesign.

Reason: Thank you all for your designs.
So far all your designs are ok but it isn´t what we are looking for. Most of the designs are too loaded, too many colors and too much decoration.

Target Market(s)

Adults of various age groups and different nationalities mostly European.

Industry/Entity Type

Restaurant

Requirements
Must have
• The menu must have two interior pages with the text as in the document attached.It must be easily legible.
Nice to have
• See what kind of menus they use in important restaurants in places like Paris, see what designs are in trend, but Not necessarily doing the same style if it doesn’t fit in with the description above.
Should not have
• Nothing old fashioned.

```html
<!DOCTYPE html>
<html lang="en">
<head>
<meta charset="utf-8">
<title>la Velada — Menu</title>
<link href="https://fonts.googleapis.com/css2?family=Great+Vibes&display=swap" rel="stylesheet">
<style>
  :root {
    --magenta: #c8197f;
    --magenta-deep: #8c0f55;
    --plum: #930f5b;
    --plum-soft: #a3146a;
    --ink: #0d0609;
    --gold: #d8b56c;
    --gold-light: #f1dca4;
    --white: #ffffff;
  }
  * { margin: 0; padding: 0; box-sizing: border-box; }
  html, body {
    width: 904px;
    height: 1200px;
    overflow: hidden;
    background: var(--magenta-deep);
  }
  .menu-cover {
    position: relative;
    width: 904px;
    height: 1200px;
    background: radial-gradient(ellipse 75% 65% at 50% 60%, var(--magenta) 0%, #b01570 55%, var(--magenta-deep) 100%);
    overflow: hidden;
  }
  .gold-frame {
    position: absolute;
    inset: 20px;
    border: 4px solid var(--gold);
    box-shadow: inset 0 0 0 2px var(--gold-light);
  }
  .crest-band {
    position: absolute;
    left: 24px;
    right: 24px;
    top: 258px;
    height: 190px;
    background: var(--plum);
  }
  .crest-halo {
    position: absolute;
    left: 232px;
    top: 143px;
    width: 440px;
    height: 440px;
    border-radius: 50%;
    background: var(--plum);
  }
  .crest-seal {
    position: absolute;
    left: 282px;
    top: 193px;
    width: 340px;
    height: 340px;
    border-radius: 50%;
    background: var(--ink);
    border: 7px solid var(--gold);
    box-shadow: 0 0 0 2px var(--gold-light);
    display: flex;
    align-items: center;
    justify-content: center;
  }
  .brand-name {
    font-family: "Great Vibes", cursive;
    font-weight: 400;
    font-size: 78px;
    color: var(--white);
    line-height: 1;
  }
  .menu-badge {
    position: absolute;
    left: 350px;
    top: 913px;
    width: 204px;
    height: 204px;
    border-radius: 50%;
    background: var(--plum-soft);
    display: flex;
    align-items: center;
    justify-content: center;
  }
  .menu-title {
    font-family: "Great Vibes", cursive;
    font-weight: 400;
    font-size: 92px;
    color: var(--white);
    line-height: 1;
  }
</style>
</head>
<body>
  <main class="menu-cover">
    <div class="gold-frame"></div>
    <div class="crest-band"></div>
    <div class="crest-halo"></div>
    <div class="crest-seal">
      <span class="brand-name">la Velada</span>
    </div>
    <div class="menu-badge">
      <h1 class="menu-title">Menu</h1>
    </div>
  </main>
</body>
</html>
```